Marlowe Holdings LLC - Business Cards

Need the following information on the cards:

Name: Dean R Vossler
Title: Chief Executive Manager

Business address:
412 N Ridgeview Lane #118
Elm Crossing, Il 60412

Phone: (630) 555-0148 - Business
KPV FFL license number: 5-21-xxx-xx-xx-04519
Email: dean.vossler@marloweholdingsffl.com

Target Market(s)

Firearm owners

Industry/Entity Type

Firearms industry,

Contact Information for Business Card

Contact number, name and title, web page address, email, business address and kpv license number,

Requirements
Must have
• Name, title, business address, phone numbers, KPV license numbers, web page address and email address.
Nice to have
• Cellphone number,

```html
<!DOCTYPE html>
<html lang="en">
<head>
<meta charset="utf-8">
<title>Marlowe Holdings LLC – Business Cards</title>
<link rel="stylesheet" href="https://fonts.googleapis.com/css2?family=Fira+Sans+Condensed:ital,wght@0,400;0,600;0,700;1,400&display=swap">
<style>
  :root {
    --backdrop: #c9c9c9;
    --brand-red: #d60000;
    --ink: #111111;
    --paper: #ffffff;
  }
  * { margin: 0; padding: 0; box-sizing: border-box; }
  html, body {
    width: 1200px; height: 846px; overflow: hidden;
    background: var(--backdrop);
    font-family: "Fira Sans Condensed", "Arial Narrow", sans-serif;
  }
  .card {
    position: absolute;
    width: 291px; height: 508px;
    border-radius: 30px;
  }
  .card--front { left: 278px; top: 171px; background: var(--brand-red); }
  .card--back {
    left: 634px; top: 169px;
    background: var(--paper);
    border: 1px solid var(--ink);
    color: var(--ink);
    text-align: center;
  }
  .brand-mark {
    position: absolute; left: 0; width: 100%;
    display: flex; flex-direction: column; align-items: center;
  }
  .brand-mark__circle {
    border-radius: 50%;
    border: 3px solid currentColor;
  }
  .brand-mark__name {
    font-weight: 700;
    font-size: 22px;
    letter-spacing: 1px;
    text-transform: uppercase;
    margin-top: 12px;
    white-space: nowrap;
  }
  .card--front .brand-mark { top: 150px; color: var(--paper); }
  .card--front .brand-mark__circle { width: 110px; height: 110px; }
  .card--back .brand-mark { top: 34px; color: var(--brand-red); }
  .card--back .brand-mark__circle { width: 96px; height: 96px; border-color: var(--ink); }
  .card--back .brand-mark__name { font-size: 21px; }

  .holder { position: absolute; left: 0; width: 100%; top: 198px; }
  .holder__name { font-size: 30px; font-weight: 700; line-height: 34px; letter-spacing: -0.3px; }
  .holder__title { font-size: 15px; font-weight: 700; color: var(--brand-red); line-height: 18px; }
  .license { position: absolute; left: 0; width: 100%; top: 257px; font-style: italic; font-size: 15px; line-height: 19px; }

  .divider { position: absolute; left: 0; width: 100%; display: block; }
  .divider--phone { top: 305px; }
  .divider--web { top: 383px; }

  .phones { position: absolute; top: 337px; left: 0; width: 100%; font-size: 15px; line-height: 18px; }
  .phones__row { display: flex; justify-content: flex-end; padding-right: 72px; }
  .phones__label { margin-right: 5px; }

  .online { position: absolute; top: 414px; left: 0; width: 100%; font-size: 14.5px; line-height: 19px; }
  .address { position: absolute; top: 457px; left: 0; width: 100%; font-size: 15px; line-height: 18px; }
</style>
</head>
<body>
  <section class="card card--front" aria-label="Card front">
    <div class="brand-mark">
      <div class="brand-mark__circle"></div>
      <div class="brand-mark__name">Marlowe Holdings LLC</div>
    </div>
  </section>

  <section class="card card--back" aria-label="Card back">
    <div class="brand-mark">
      <div class="brand-mark__circle"></div>
      <div class="brand-mark__name">Marlowe Holdings LLC</div>
    </div>

    <div class="holder">
      <div class="holder__name">Dean R Vossler</div>
      <div class="holder__title">CHIEF EXECUTIVE MANAGER</div>
    </div>

    <div class="license">KPV FFL license number:<br>5-21-xxx-xx-xx-04519</div>

    <svg class="divider divider--phone" width="291" height="28" viewBox="0 0 291 28" aria-hidden="true">
      <polygon points="57,14 122,12 122,16" fill="#111"/>
      <polygon points="167,12 232,14 167,16" fill="#111"/>
      <path d="M136,4 q-6,0 -6,10 q0,10 6,10 l2,-4 q-3,-1 -3,-6 q0,-5 3,-6 z" fill="#d60000"/>
      <rect x="147" y="3" width="11" height="22" rx="2" fill="none" stroke="#d60000" stroke-width="1.6"/>
      <rect x="149.5" y="6" width="6" height="5" fill="none" stroke="#d60000" stroke-width="1.2"/>
      <g fill="#d60000"><rect x="149.5" y="14" width="6" height="1.4"/><rect x="149.5" y="17" width="6" height="1.4"/><rect x="149.5" y="20" width="6" height="1.4"/></g>
    </svg>

    <div class="phones">
      <div class="phones__row"><span class="phones__label">Phone:</span><span>(630) 555-0148</span></div>
      <div class="phones__row"><span class="phones__label">Cellphone:</span><span>(630) 555-0193</span></div>
    </div>

    <svg class="divider divider--web" width="291" height="28" viewBox="0 0 291 28" aria-hidden="true">
      <polygon points="33,14 98,12 98,16" fill="#111"/>
      <polygon points="191,12 256,14 191,16" fill="#111"/>
      <g fill="none" stroke="#d60000" stroke-width="1.6">
        <rect x="104" y="7" width="21" height="14"/>
        <polyline points="104,7 114.5,16 125,7"/>
        <circle cx="147" cy="14" r="10"/>
        <ellipse cx="147" cy="14" rx="4.5" ry="10"/>
        <line x1="137" y1="14" x2="157" y2="14"/>
        <line x1="139" y1="9" x2="155" y2="9"/>
        <line x1="139" y1="19" x2="155" y2="19"/>
        <path d="M175,25 q-8,-10 -8,-15 a8,8 0 0 1 16,0 q0,5 -8,15 z"/>
        <circle cx="175" cy="10" r="3"/>
      </g>
    </svg>

    <div class="online">dean.vossler@marloweholdingsffl.com<br>www.marloweholdingsffl.com</div>
    <div class="address">412 N Ridgeview Lane #118<br>Elm Crossing, Il 60412</div>
  </section>
</body>
</html>
```